Craft oriented film company needs a Business Card design

Hi all,
We're a 2-man band film company in New Zealand called Kestrel Pictures. We're good honest blokes, who are very passionate about the craft of film making. I've attached our current logo which has a bit of a crafty/artisan feel that we like. Feel free to use it - or throw the baby out with the bathwater and start again..... you never know, you might inspire a complete brand re-work.

In any case, the vibe we want to give out is that we are solid, dependable and no bullshit - but without compromising creative excellence and being in the now. We like the 'Brooklyn' artisan style of work.

Preferably single sided.

We need the standard stuff:
Name, job title, cellphone, email address and physical address (this can be smaller if you like - street, suburb, city & zip, country [if you want])

Check out our website to learn more about us: kestrelpictures.example

Target Market(s)

Brand marketers and advertising agency creatives looking for video production.

Industry/Entity Type

Baby

Requirements
Should not have
• Nothing flashy or too 'futuristic', we want it to feel grounded and real. A limited colour palette is preferred.
We don't want any film reels or cameras or anything obvious like that.

```html
<!DOCTYPE html>
<html lang="en">
<head>
<meta charset="utf-8">
<title>Kestrel Pictures – Business Card</title>
<link rel="stylesheet" href="https://fonts.googleapis.com/css2?family=Mulish:wght@400;600;800&display=swap">
<style>
  :root {
    --page-bg: #e9e7e4;
    --card-bg: #ffffff;
    --ink: #111111;
    --ink-soft: #4a4a4a;
    --strip: #4b4b4b;
    --shadow: rgba(0, 0, 0, 0.18);
  }
  * { box-sizing: border-box; margin: 0; padding: 0; }
  html, body {
    width: 1200px;
    height: 1200px;
    overflow: hidden;
    background: var(--page-bg);
    font-family: "Mulish", "Century Gothic", sans-serif;
    color: var(--ink);
  }
  .canvas {
    width: 1200px;
    height: 1200px;
    display: flex;
    align-items: center;
    justify-content: center;
  }
  .business-card {
    position: relative;
    width: 1050px;
    height: 600px;
    background: var(--card-bg);
    box-shadow: 0 18px 40px var(--shadow);
    overflow: hidden;
  }
  .film-texture {
    position: absolute;
    inset: 0;
    width: 100%;
    height: 100%;
  }
  .brand {
    position: absolute;
    top: 120px;
    right: 60px;
    display: flex;
    align-items: center;
    gap: 16px;
  }
  .brand-dot {
    width: 44px;
    height: 44px;
    border-radius: 50%;
    background: var(--ink);
  }
  .brand-name {
    font-weight: 800;
    font-size: 30px;
    color: var(--ink);
    white-space: nowrap;
  }
  .identity {
    position: absolute;
    left: 225px;
    top: 218px;
  }
  .person-name {
    font-weight: 800;
    font-size: 40px;
    line-height: 1.1;
  }
  .job-title {
    font-weight: 800;
    font-size: 21px;
    color: var(--ink-soft);
    margin-top: 2px;
  }
  .contact-list {
    position: absolute;
    left: 210px;
    top: 340px;
    list-style: none;
    font-size: 25px;
    line-height: 1.45;
  }
  .website {
    position: absolute;
    right: 70px;
    bottom: 40px;
    font-size: 27px;
    font-weight: 600;
  }
</style>
</head>
<body>
<main class="canvas">
  <article class="business-card">
    <svg class="film-texture" viewBox="0 0 1050 600" aria-hidden="false">
      <polygon role="img" aria-label="Grunge film strip texture across the top edge"
        fill="var(--strip)"
        points="0,40 740,0 760,95 0,150"/>
      <polygon role="img" aria-label="Grunge film strip texture along the lower left corner"
        fill="var(--strip)"
        points="0,270 70,250 250,600 110,600 0,420"/>
    </svg>

    <div class="brand">
      <span class="brand-dot"></span>
      <span class="brand-name">Kestrel Pictures</span>
    </div>

    <header class="identity">
      <h1 class="person-name">Rowan Hale</h1>
      <p class="job-title">Designer</p>
    </header>

    <ul class="contact-list">
      <li class="contact-phone">Cellphone : 0712358640</li>
      <li class="contact-email">Email : hello@kestrelpictures.example</li>
      <li class="contact-address">Address : your street, suburb, city &amp; zip, country</li>
    </ul>

    <p class="website">www.kestrelpictures.example</p>
  </article>
</main>
</body>
</html>
```